Corrandel Ice Creamery tourist signage

We need to give passing tourists a snapshot of what great fun they can have visiting our brand new Ice creamery located in Timboon, 17km North of the Great Ocean Road and Famous 12 Apostles in Victoria Australia. So the sign needs to be more than directional, need to be enticing. needs to be designed in a manner that project quality. ( keep in mind cars travelling at 80km don't have a lot of time to read too much)
Size is 2.2metres wide by 1.4 meters high
This sign needs to be succinct. Needs to convey fun and a little indulgence but not in a 'tacky' or 'cheap' way.
Needs to offer indulgent imagery of course, our logo too and direction.

Target Market(s)

Tourists, domestic and internationals

Industry/Entity Type

Tourism

Other font styles liked:
• sacred cow

Colors
add136
fdf3f8
b8a6cd
fabb94
fcca95
85acd3
fbf289

Requirements
Must have
• Convey fun, whimsy indulgence and value ( keeping in mind we need to entice these people a further 17km up the road!)
Nice to have
• White space and clear imagery with
Should not have
• Bold bling colours, be busy looking and cheap looking, needs to convey quality .

```html
<!DOCTYPE html>
<html lang="en">
<head>
<meta charset="utf-8">
<title>Corrandel Ice Creamery – Roadside Sign</title>
<link href="https://fonts.googleapis.com/css2?family=Amatic+SC:wght@700&display=swap" rel="stylesheet">
<style>
  :root {
    --page: #ffffff;
    --paper: #efe9df;
    --ink: #1c1a17;
    --pink: #eab0c6;
    --yellow: #f6ef8c;
    --peach: #f4c79c;
    --coral: #e8948f;
    --green: #9cc83f;
    --green-soft: #a8c94c;
    --sky: #a6d3dc;
    --lilac: #cab7d8;
  }
  html, body {
    margin: 0;
    padding: 0;
    width: 1200px;
    height: 1000px;
    overflow: hidden;
    background: var(--page);
  }
  .canvas {
    position: relative;
    width: 1200px;
    height: 1000px;
  }
  .sign {
    position: absolute;
    left: 90px;
    top: 147px;
    width: 1033px;
    height: 657px;
    overflow: hidden;
    background: radial-gradient(ellipse at 40% 40%, #f3eee6 0%, var(--paper) 70%, #e8e0d3 100%);
    font-family: "Amatic SC", cursive;
    color: var(--ink);
  }
  .sign-art {
    position: absolute;
    inset: 0;
  }
  .sign-text {
    position: absolute;
    left: 0;
    width: 100%;
    text-align: center;
    margin: 0;
    font-weight: 700;
    line-height: 1;
  }
  .tagline {
    top: 68px;
    left: 15px;
    font-size: 44px;
    letter-spacing: 2px;
    transform: rotate(-3deg);
  }
  .brand-name {
    top: 200px;
    left: 10px;
    font-size: 116px;
    letter-spacing: 6px;
  }
  .brand-sub {
    top: 318px;
    left: 10px;
    font-size: 54px;
    letter-spacing: 5px;
  }
  .distance {
    top: 440px;
    left: 30px;
    font-size: 78px;
    letter-spacing: 3px;
  }
  .destination {
    top: 525px;
    left: 30px;
    font-size: 40px;
    letter-spacing: 3px;
  }
</style>
</head>
<body>
<main class="canvas">
  <section class="sign" aria-label="Corrandel Ice Creamery roadside sign">
    <svg class="sign-art" viewBox="0 0 1033 657" width="1033" height="657" aria-hidden="true">
      <g class="dots" opacity="0.9">
        <circle cx="230" cy="63" r="72" fill="var(--pink)"/>
        <circle cx="275" cy="98" r="45" fill="var(--pink)"/>
        <circle cx="685" cy="68" r="115" fill="var(--yellow)"/>
        <circle cx="750" cy="93" r="50" fill="var(--yellow)"/>
        <circle cx="985" cy="68" r="70" fill="var(--peach)"/>
        <circle cx="28" cy="261" r="11" fill="var(--coral)"/>
        <circle cx="70" cy="353" r="55" fill="var(--coral)"/>
        <circle cx="125" cy="315" r="48" fill="var(--coral)"/>
        <circle cx="760" cy="367" r="21" fill="var(--green-soft)"/>
        <circle cx="878" cy="403" r="68" fill="var(--green-soft)"/>
        <circle cx="814" cy="496" r="18" fill="var(--sky)"/>
        <circle cx="880" cy="633" r="90" fill="var(--sky)"/>
        <circle cx="970" cy="598" r="85" fill="var(--sky)"/>
        <circle cx="90" cy="613" r="70" fill="var(--peach)"/>
        <circle cx="20" cy="643" r="55" fill="var(--peach)"/>
        <circle cx="400" cy="643" r="45" fill="var(--lilac)"/>
        <circle cx="460" cy="643" r="45" fill="var(--lilac)"/>
      </g>
      <circle class="brand-dot" cx="500" cy="268" r="140" fill="var(--green)"/>
      <path class="dashed-frame" d="M33 23 L1012 50 L993 622 L18 632 Z"
            fill="none" stroke="var(--ink)" stroke-width="3" stroke-dasharray="14 10" stroke-linejoin="round"/>
    </svg>

    <p class="sign-text tagline">Farm fresh daily!</p>
    <h1 class="sign-text brand-name">Corrandel</h1>
    <p class="sign-text brand-sub">Ice Creamery</p>
    <p class="sign-text distance">17km North</p>
    <p class="sign-text destination">Visitor Centre</p>
  </section>
</main>
</body>
</html>
```